Fast Growing Personal Injury Law Firm Needs Business Card Design

We need a business card design for a fast growing personal injury law firm in Florida. Our name is Dorian Halvorsk, P.A. Our practice is comprised of younger attorneys (in their 30s) that employ more modern techniques/tools than our older competition. We would prefer a look that is a modern play on a classic look. Also, we would like to continue using a color scheme that employs navy blue and kelly green (other shades of green could be fine too) as well as our "E" logo.

Industry/Entity Type

Law Firm

```html
<!DOCTYPE html>
<html lang="en">
<head>
<meta charset="utf-8">
<title>Dorian Halvorsk, P.A. — Stationery</title>
<link rel="stylesheet" href="https://fonts.googleapis.com/css2?family=Cinzel:wght@500&family=Lato:wght@400;700&family=Allura&display=swap">
<style>
  :root {
    --navy: #1b3a6b;
    --green: #2e8b3e;
    --paper: #ffffff;
    --ground: #e8e6e7;
    --ink: #2b2b2b;
    --muted: #555a60;
  }
  * { margin: 0; padding: 0; box-sizing: border-box; }
  html, body { width: 1200px; height: 1200px; overflow: hidden; }
  body { background: var(--ground); font-family: "Lato", sans-serif; color: var(--ink); position: relative; }

  .letterhead { position: absolute; left: 72px; top: 116px; width: 696px; height: 978px; background: var(--paper); box-shadow: 0 2px 6px rgba(0,0,0,.12); }
  .brand { position: absolute; display: flex; align-items: center; gap: 12px; }
  .brand-mark { background: var(--green); flex: none; }
  .brand-name { font-family: "Cinzel", serif; font-weight: 500; color: var(--navy); line-height: 1; white-space: nowrap; }
  .brand-tagline { font-family: "Cinzel", serif; font-weight: 500; color: var(--green); line-height: 1; white-space: nowrap; letter-spacing: .06em; }

  .letterhead .brand { left: 72px; top: 88px; }
  .letterhead .brand-mark { width: 60px; height: 56px; }
  .letterhead .brand-name { font-size: 22px; }
  .letterhead .brand-tagline { font-size: 14px; margin-top: 6px; }

  .letter-contact { position: absolute; right: 72px; top: 78px; text-align: right; font-size: 10px; line-height: 12.5px; color: var(--muted); }
  .letter-contact .gap { height: 8px; }
  .contact-line { display: flex; justify-content: flex-end; align-items: center; gap: 4px; }
  .dot-icon { width: 9px; height: 9px; flex: none; }

  .letter-body { position: absolute; left: 73px; top: 224px; width: 552px; font-size: 12.4px; line-height: 16.2px; color: var(--ink); }
  .letter-body p { margin-bottom: 16.2px; }
  .recipient { font-weight: 700; }
  .subject { font-weight: 700; }
  .signature { font-family: "Allura", cursive; font-size: 24px; line-height: 24px; color: #444; margin: 8px 0 6px; }
  .signer { line-height: 16.2px; }

  .letter-footer { position: absolute; left: 0; bottom: 0; width: 696px; height: 30px; }
  .letter-url { position: absolute; right: 16px; bottom: 6px; color: #fff; font-size: 15px; }

  .card { position: absolute; width: 322px; height: 180px; box-shadow: 0 2px 5px rgba(0,0,0,.15); overflow: hidden; }
  .card-front { left: 812px; top: 179px; background: var(--navy); }
  .card-front-split { position: absolute; inset: 0; }
  .card-front-text { position: absolute; right: 8px; bottom: 8px; text-align: right; color: #fff; }
  .card-front-name { font-family: "Cinzel", serif; font-size: 14px; }
  .card-front-tagline { font-family: "Cinzel", serif; font-size: 9px; letter-spacing: .08em; margin-top: 3px; }
  .card-front-url { font-family: "Cinzel", serif; font-size: 8px; letter-spacing: .22em; margin-top: 4px; }

  .card-back { left: 812px; top: 422px; height: 178px; background: var(--paper); }
  .card-back .brand { left: 38px; top: 28px; gap: 8px; }
  .card-back .brand-mark { width: 46px; height: 40px; }
  .card-back .brand-name { font-size: 15px; }
  .card-back .brand-tagline { font-size: 10px; margin-top: 4px; }
  .card-person { position: absolute; left: 36px; top: 95px; width: 140px; }
  .person-name { color: var(--navy); font-size: 11px; }
  .person-title { font-size: 8px; color: var(--muted); padding-bottom: 3px; border-bottom: 1px solid #999; margin-bottom: 5px; }
  .person-address { font-size: 8px; line-height: 11px; color: var(--muted); }
  .card-divider { position: absolute; left: 183px; top: 96px; width: 1px; height: 44px; background: #aaa; }
  .card-contact { position: absolute; left: 198px; top: 94px; font-size: 8px; line-height: 13.5px; color: var(--muted); }
  .card-contact .contact-line { justify-content: flex-start; }
  .card-band { position: absolute; left: 0; bottom: 0; width: 322px; height: 12px; }
</style>
</head>
<body>

  <section class="letterhead">
    <div class="brand">
      <div class="brand-mark"></div>
      <div>
        <div class="brand-name">Dorian Halvorsk, P.A.</div>
        <div class="brand-tagline">Personal Injury Attorneys</div>
      </div>
    </div>

    <div class="letter-contact">
      <div>2215 Harbor Crest Drive Suite 410</div>
      <div>Palm Grove, Florida 34118</div>
      <div class="gap"></div>
      <div class="contact-line">555.310.2841 <svg class="dot-icon" viewBox="0 0 10 10"><circle cx="5" cy="5" r="5" fill="var(--navy)"/><path d="M3 2.6l1 1-.5.7c.4.8 1 1.4 1.8 1.8l.7-.5 1 1-.6.8C4.8 7.2 2.8 5.2 2.6 3.2z" fill="#fff"/></svg></div>
      <div class="contact-line">555.310.2842 <svg class="dot-icon" viewBox="0 0 10 10"><circle cx="5" cy="5" r="5" fill="var(--navy)"/><rect x="3" y="3" width="4" height="4" fill="#fff"/></svg></div>
      <div class="contact-line">dorian@halvorsklaw.com <svg class="dot-icon" viewBox="0 0 10 10"><circle cx="5" cy="5" r="5" fill="var(--navy)"/><rect x="2.6" y="3.2" width="4.8" height="3.6" fill="#fff"/><path d="M2.6 3.2L5 5.2 7.4 3.2" stroke="var(--navy)" stroke-width=".6" fill="none"/></svg></div>
    </div>

    <div class="letter-body">
      <div class="recipient">Mr. John Doe</div>
      <p class="recipient">President</p>
      <p class="subject">Subject: Introduction Letter</p>
      <p>Greetings</p>
      <p>Lorem ipsum dolor sit amet, consectetur adipiscing elit. Integer malesuada velit eget venenatis sollicitudin. Nunc molestie pharetra metus. Morbi feugiat elit auctor orci congue, non ultricies est facilisis. Nullam lacinia quis orci non ultrices. Aliquam quam mauris, vulputate eu condimentum non, dictum vel erat. Pellentesque quis odio erat. Duis feugiat, elit vel bibendum malesuada, sem est semper massa, id fermentum diam risus sit amet tortor.</p>
      <p>Pellentesque posuere ut tellus vitae scelerisque. Curabitur sed arcu sit amet lectus porta scelerisque ac eu neque. Nunc dapibus mauris massa, nec auctor odio aliquet a. Nullam eu tempor libero. Nam vitae consequat lectus. Curabitur sed adipiscing velit. Donec non sapien id nulla ornare placerat fringilla sed nisi.</p>
      <p>Mauris orci elit, accumsan nec orci a, feugiat gravida purus. Proin porttitor mattis gravida. Aenean blandit massa dapibus erat porttitor hendrerit. Morbi ut dui justo. Vestibulum felis dui, volutpat ut laoreet eget, gravida a velit. Pellentesque placerat suscipit quam, in mollis elit accumsan id. Curabitur ac suscipit est. Sed fringilla nibh non leo porta rutrum. Vestibulum porta nibh elit, a feugiat sem gravida eu. Nullam in ligula vel mi tincidunt sagittis. Nulla et elementum justo, sed consequat diam. Donec nec semper nibh. Nulla faucibus mauris quis fermentum consequat. Etiam dapibus neque ipsum, id dapibus leo luctus sed. Maecenas ut pulvinar dolor.</p>
      <p>Proin id pulvinar dolor. Praesent posuere purus quis fringilla condimentum. Aenean rhoncus, metus at porta ultrices, nisi velit euismod enim, vitae varius quam velit in mi. Nunc eget rutrum erat. Aenean vel cursus diam. Sed laoreet metus et tortor malesuada, at suscipit neque molestie. Mauris sed malesuada diam, in vulputate metus. In hac habitasse platea dictumst.</p>
      <div style="height:14px"></div>
      <div>Regards,</div>
      <div class="signature">your signature</div>
      <div class="signer">Reyna Castillo</div>
      <div class="signer">Executive Director</div>
    </div>

    <svg class="letter-footer" viewBox="0 0 696 30" preserveAspectRatio="none">
      <polygon points="0,0 512,0 506,8 0,8" fill="var(--green)"/>
      <polygon points="0,8 506,8 512,0 696,0 696,30 0,30" fill="var(--navy)"/>
    </svg>
    <div class="letter-url">www.halvorsklaw.com</div>
  </section>

  <section class="card card-front">
    <svg class="card-front-split" viewBox="0 0 322 180" preserveAspectRatio="none">
      <path d="M0,0 H150 C110,50 100,120 130,180 H0 Z" fill="var(--green)"/>
    </svg>
    <div class="card-front-text">
      <div class="card-front-name">Dorian Halvorsk, P.A.</div>
      <div class="card-front-tagline">Personal Injury Attorneys</div>
      <div class="card-front-url">www.halvorsklaw.com</div>
    </div>
  </section>

  <section class="card card-back">
    <div class="brand">
      <div class="brand-mark"></div>
      <div>
        <div class="brand-name">Dorian Halvorsk, P.A.</div>
        <div class="brand-tagline">Personal Injury Attorneys</div>
      </div>
    </div>
    <div class="card-person">
      <div class="person-name">Dorian Halvorsk</div>
      <div class="person-title">Attorney at Law</div>
      <div class="person-address">2215 Harbor Crest Drive Suite 410<br>Palm Grove, Florida 34118</div>
    </div>
    <div class="card-divider"></div>
    <div class="card-contact">
      <div class="contact-line"><svg class="dot-icon" viewBox="0 0 10 10"><circle cx="5" cy="5" r="5" fill="var(--navy)"/><path d="M3 2.6l1 1-.5.7c.4.8 1 1.4 1.8 1.8l.7-.5 1 1-.6.8C4.8 7.2 2.8 5.2 2.6 3.2z" fill="#fff"/></svg> 555.310.2841</div>
      <div class="contact-line"><svg class="dot-icon" viewBox="0 0 10 10"><circle cx="5" cy="5" r="5" fill="var(--navy)"/><rect x="3" y="3" width="4" height="4" fill="#fff"/></svg> 555.310.2842</div>
      <div class="contact-line"><svg class="dot-icon" viewBox="0 0 10 10"><circle cx="5" cy="5" r="5" fill="var(--navy)"/><rect x="2.6" y="3.2" width="4.8" height="3.6" fill="#fff"/></svg> dorian@halvorsklaw.com</div>
      <div class="contact-line"><svg class="dot-icon" viewBox="0 0 10 10"><circle cx="5" cy="5" r="5" fill="var(--navy)"/><circle cx="5" cy="5" r="2.4" fill="none" stroke="#fff" stroke-width=".8"/></svg> www.halvorsklaw.com</div>
    </div>
    <svg class="card-band" viewBox="0 0 322 12" preserveAspectRatio="none">
      <polygon points="0,0 172,0 166,8 0,8" fill="var(--green)"/>
      <polygon points="0,8 166,8 172,0 322,0 322,12 0,12" fill="var(--navy)"/>
    </svg>
  </section>

</body>
</html>
```